Harbor Steadfast Wellness Foundation branding and promotion

I need a brochure (not the typical trifold (maybe 5X5 with 5 or 6 segments). It needs to deliver several strong points: who we are, why we exist, what we do, how we do it, and DONATE now.We are a fairly new Foundation in the Veteran space, a very crowded space. I need a design that will separate us and clearly state: who we are (our story), what we do, how we do it and why. Our website is www.hswf-demo.example

Target Market(s)

Corporate America, Veterans, their family members, the members of the community where they live, work, play and pray

Font styles to use
Serif

Colors
ffc214
faa54b
f68d4d
e34197

Requirements
Must have
• "CURB APPEAL", it must grab the target market and COMPEL them to volunteer, donate, sponsor foundation activities.
• Pictures
• Graphics
• Review website for content, I will then expand, edit, etc.
Nice to have
• For colors, see the colors in the logo. Other complementary colors can be used

```html
<!DOCTYPE html>
<html lang="en">
<head>
<meta charset="utf-8">
<title>Harbor Steadfast Wellness Foundation – Brochure</title>
<link rel="stylesheet" href="https://fonts.googleapis.com/css2?family=Montserrat+Alternates:ital,wght@1,700&family=Tinos:wght@400;700&display=swap">
<style>
:root{
  --yellow:#ffc214;
  --magenta:#e0368f;
  --ink:#222;
  --body:#3a3a3a;
  --backdrop:#8c8c8c;
  --paper:#ffffff;
}
*{box-sizing:border-box;margin:0;padding:0}
html,body{width:1200px;height:1200px;overflow:hidden}
body{background:var(--backdrop);position:relative;font-family:"Tinos","Times New Roman",serif;color:var(--body)}
.sheet{position:absolute;left:99px;width:1003px;height:501px;background:var(--paper);overflow:hidden;box-shadow:0 2px 8px rgba(0,0,0,.35)}
.sheet--outer{top:95px}
.sheet--inner{top:603px}
.block{position:absolute}
.yellow-band{background:var(--yellow)}
.display{font-family:"Montserrat Alternates",sans-serif;font-style:italic;font-weight:700;color:var(--magenta)}
.tab{position:absolute;background:var(--magenta);color:#fff;font-family:"Montserrat Alternates",sans-serif;font-style:italic;font-weight:700;padding-left:31px;display:flex;align-items:center}
.col p{font-size:8.8px;line-height:11.8px;margin-bottom:6px}
.col h3{font-size:13.5px;line-height:17px;margin:4px 0 5px}
.about p{font-size:10.4px;line-height:13.4px;margin-bottom:6px;color:#333}
.ring{position:absolute;border-radius:50%;background:#fff}
.ring::before{content:"";position:absolute;inset:5px;border-radius:50%;border:1.5px dashed #8a8a8a}
.ring .photo{position:absolute;inset:11px;border-radius:50%}
.mission p{font-size:8.8px;line-height:11.8px;margin-bottom:6px;color:#222}
.vision ul{list-style:none}
.vision li{position:relative;padding-left:15px;font-size:8.8px;line-height:11.8px;margin-bottom:4px}
.vision li::before{content:"";position:absolute;left:1px;top:4px;width:4px;height:4px;border-radius:50%;background:#333}
</style>
</head>
<body>

<section class="sheet sheet--outer">
  <div class="block yellow-band" style="left:0;top:0;width:501px;height:264px"></div>

  <div class="ring" style="left:53px;top:-115px;width:236px;height:236px">
    <div class="photo" role="img" aria-label="Photo of a multigenerational military family with a soldier in uniform" style="background:linear-gradient(135deg,#3c3a44,#8a6b58 55%,#c9a07e)"></div>
  </div>
  <div class="ring" style="left:265px;top:-33px;width:234px;height:234px">
    <div class="photo" role="img" aria-label="Photo of two smiling mothers holding a baby" style="background:linear-gradient(135deg,#d8c7b6,#c99b80 50%,#6f8fb8)"></div>
  </div>

  <h1 class="block display" style="left:31px;top:130px;font-size:15px;line-height:21px;white-space:nowrap">Military children have<br>more healthcare needs, but<br>less access and lower quality</h1>
  <h2 class="block" style="left:31px;top:194px;font-size:14px;font-weight:700;color:var(--ink)">Quality Care for Children of Veterans</h2>
  <p class="block" style="left:31px;top:216px;width:415px;font-size:10.4px;line-height:13.4px;color:#111">Children in military families insured by SentryCare are more likely to have special health care needs, and more likely to have a behavioral health diagnosis compared to their civilian peers, according to a new study.</p>

  <div class="tab" style="left:0;top:264px;width:103px;height:26px;font-size:16px">ABOUT</div>

  <div class="block about" style="left:31px;top:294px;width:130px">
    <p>Harbor Steadfast Wellness Foundation (HSWF) is a non-profit 501c3 charitable entity established in 2013 by military veterans with expertise in healthcare, for the express purpose of addressing systemic inequities regarding access to and quality of care for veterans and their families.</p>
    <p>Having committed their lives to our country,</p>
  </div>
  <div class="block about" style="left:183px;top:294px;width:140px">
    <p>Veterans leave military service with a host of potentially debilitating health conditions—not just PTSD and traumatic brain injury, but autoimmune disorders, hearing loss, lung disorders, chemical exposure related heart problems, musculoskeletal injuries, and a host of other potential problems many that remain unknown for years after</p>
  </div>
  <div class="block about" style="left:335px;top:294px;width:135px">
    <p>discharge or retirement.</p>
    <p>Then they enter the veterans’ and/or civilian healthcare system where many of the providers, allied healthcare professionals and support services personnel are largely unprepared to diagnose, treat and manage their service-related health issues.</p>
  </div>

  <div class="block col" style="left:532px;top:33px;width:212px">
    <h3 class="display">Healthcare Education and Training</h3>
    <p>Contributing to our healthcare education and training initiatives will directly impact healthcare providers, allied healthcare professionals and veterans themselves.</p>
    <p>The HSW Foundation has partnered with Northfield Learning Partners (NLP, Inc), ClearPath eLearning, and Steadfast Health Academy to provide veteran centric and cultural competency training to enhance their knowledge and understanding of veteran culture and its impact on healthcare delivery and health outcomes of veterans and their families.</p>
    <h3 class="display">Community Health and Wellness Engagement Events</h3>
    <p>Contributing to community engagement facilitate the sponsorship of projects and events to cultivate awareness and understanding of the unique healthcare needs of veteran and their families.</p>
    <p>The HSW Foundation strives to empower veterans and communities to become part of the solution and work to educate others in their communities. Your donation would fund free healthcare screenings, flu shots, medical appointments or a speaker(s) for a community health and wellness forum.</p>
    <h3 class="display">Health and Wellness Education Forums</h3>
    <p>Contributing to healthcare awareness and education forums and events that facilitate the evolution of people in the community and their leaders from</p>
  </div>

  <div class="block col" style="left:760px;top:33px;width:212px">
    <p>supporters to savvy advocates for the healthcare needs of veterans and their families. Civilian healthcare facilities, when asked, are not aware that veterans are being served in their clinics, hospitals and medical centers.</p>
    <p>Your donation will help break through this misconception and others regarding the health and healthcare needs of veterans and their families raising the bar for both the community and healthcare facilities.</p>
    <h3 class="display">Harbor Steadfast Wellness Foundation (HSWF) and the Veteran Care Neighborhood Consortium (VCNC)</h3>
    <p>The Harbor Steadfast Wellness Foundation (HSWF) serves as the “veteran facing” primary hub of coordination for healthcare delivery. This is achieved via two pathways, 1) clinical - through HSW authorized clinics / hospitals and recognized providers, allied healthcare professionals and social support personnel and 2) non-clinical - HSWF VCNC members / partners (i.e. community centers and their leaders, clergy, faith-based organizations, employers, public health agencies, veteran centric businesses, etc.).</p>
    <p>With the integration of HSWF as an essential core element within the medical neighborhood, the health needs of the individual (veteran), aspects of the population (their families) and overall community (where they live, work, play, and pray), the potential and opportunity for improved health and healthcare delivery (success), prompt and practical</p>
  </div>
</section>

<section class="sheet sheet--inner">
  <div class="block col" style="left:31px;top:30px;width:210px">
    <p>assessment and management of social determinants will increase significantly.</p>
    <p>The “veteran care neighborhood consortium” is a framework for structured bidirectional and cross functional relationships and partnerships (clinical and non-clinical) that integrate health / wellness, social determinants / support and medical partnerships critical to enhancing health, wellness and healthcare outcomes. The bidirectional / cross functional flow of information across and between all clinical providers and patients (i.e., primary and specialty care, physician extenders, hospitals/ clinics, home health, long term care, behavioral health, etc.) provide the framework. Non-clinical partners (i.e., community centers, faith-based organizations, employers, public health agencies, food banks, schools, etc.) provide the additional components. When combined, these partnerships actively promote health, wellness and healthcare coordination.</p>
    <p>Most of the barriers preventing veterans with complex needs from achieving better health engagement and health outcomes encompass social, mental/behavioral health, and economic factors. While providers can assess and identify these needs, the link between the veteran and the necessary resources often falls short underscoring the critical need for a resource network that includes communication between the veteran, the clinic/provider, and community organizations and businesses.</p>
    <p>As the HSWF embeds itself more firmly in the VCNC and the health environment at large, veterans, their families and their advocates will become more savvy regarding their health, healthcare, and healthcare services and delivery.</p>
  </div>
  <div class="block col" style="left:259px;top:30px;width:212px">
    <p>They expect high-quality, high-value, culturally appropriate and timely care. When this is not the case, they may become confused and/or frustrated which often leads a decrease in follow through with medications, recommendations, etc. and gaps in care ensue. It’s a similar experience noted across almost any industry providing services to consumers: the services are catered to the individual’s needs and available when the consumer needs/wants them. If not, the consumer finds a new service provider.</p>
    <p>The National Council for Care Quality (NCCQ) articulates that a successful medical neighborhood will “focus on meeting the needs of the individual patient, but also incorporate aspects of population health and overall community health needs.” The Harbor Steadfast Wellness Foundation expands this definition to include services and businesses that also address social determinants and contributors.</p>
    <p>The bi-directional and cross functionality of the model is what ensures the high, mid, and more direct levels of function of the veteran care neighborhood consortium members. In essence, the veteran care neighborhood consortium is a combination of the typical medical and geographic neighborhood integrated with collaborating partners and relationships where all participants (service members, veterans, their families, the community and its leaders, providers, allied healthcare professionals, pharmacy, labs, business owners, authorized HSW clinics and/or hospitals, etc.) must be educated to understand how to participate such that their participation optimizes their experience.</p>
  </div>

  <div class="block yellow-band" style="left:501px;top:0;width:502px;height:291px"></div>

  <div class="block mission" style="left:532px;top:36px;width:205px">
    <h3 class="display" style="font-size:16.5px;margin-bottom:5px">Our Mission</h3>
    <p>For those reasons the Harbor Steadfast Wellness Foundation was established.</p>
    <p>Now more than ever and for many reasons, Americans are less connected to their military community. And, veterans who come home feel and internalize that disconnect... some even say they feel anonymous. Because of this, America is failing to deliver on its promise...”To care for those who shall have borne the battle.”</p>
    <p>Harbor Steadfast Wellness Foundation is committed to help and to give back to the men, women and families who serve our nation – whether in uniform or not, at home or abroad, and in times of turmoil or peace.</p>
    <p>Making good America’s promise...your promise... to ensure they get the quality healthcare is a way to operationalize “Thank You for Your Service”.</p>
  </div>

  <div class="ring" style="left:745px;top:17px;width:232px;height:232px">
    <div class="photo" role="img" aria-label="Photo of a presenter speaking to a group of professionals" style="background:linear-gradient(135deg,#f2efe9,#c9b9a5 55%,#4a4f5c)"></div>
  </div>
  <div class="ring" style="left:852px;top:185px;width:210px;height:210px">
    <div class="photo" role="img" aria-label="Portrait photo of an older veteran wearing a service cap" style="background:linear-gradient(135deg,#2e3038,#7b736c 55%,#c8c3bc)"></div>
  </div>

  <div class="tab" style="left:501px;top:291px;width:145px;height:25px;font-size:15.5px">Our Vision</div>

  <div class="block vision col" style="left:532px;top:325px;width:440px">
    <p style="font-weight:700;color:#222;white-space:nowrap">HSWF envisions a world in which ALL veterans and their families live<br>healthy and well lives undiminished by their service related health concerns.</p>
    <p>HSWF approaches its vision with passion and purpose to ensure we:</p>
    <ul>
      <li>Amplify the veteran community voice in the battle for health and wellness</li>
      <li>Advocate for equitable healthcare for veterans and their families</li>
      <li>Gather and disseminate knowledge regarding veterans’ health, healthcare and wellness to veterans, their families and the communities in which they live</li>
      <li>Develop and disseminate free education and training to healthcare professionals that address the health and wellness of veterans’ and their families</li>
      <li>Continuously refine the Veteran Care Neighborhood Consortium™ model to safeguard the mission.</li>
    </ul>
  </div>
</section>

</body>
</html>
```